Company Presentation re-design.

We need to create a new 15-20 pager-presentation that will show KORVALE (travel management company) as a client-centric company with a human-to-human approach. As a start we ask a Designers to create a 3 page test presentation so we can choose the winner. who will then design the rest slides

Two main idears are to be shown on the slides:
• KORVALE is client-centric company who believes in partnership with corporate clients;
• KORVALE is a stable and trustworthy partner;

The test slides should be:

Slide (1) - Our strategy is Customer – centric strategy. KORVALE bases its business approach on the customer needs. 5 qualities that identify KORVALE as a customer-centric :
1. corporate culture, aimed at customers' changing needs
2. professional Key Account Manager (KAM)
3. Each product solution meets specific client needs.
4. innovation
5. security policy

Slide (2) - Our product solutions of clients needs
The main idea of this page is to describe our products for customers. KORVALE has 5 main products:
1. Business Travel
2. Service
3. On-line booking
4. MICE & Congress
5. Non-standard services

Slide (3)
This page shows the highlights of KORVALE support and it is shown in a cloud design now.

Attched pls find our current presentation

Dear Professionals! Please pay attantion that we updated the project by doubled the budjet! Wait for yiour grate ideas. 

Target Market(s)

Mid to top management (practically any industry), travel coordinators, procurement specialists, corporate buyers etc, travelers

Industry/Entity Type

Security

Requirements
Must have
• (1) The presentation must visualize the text above, with as little text itself as possible.
(2) We would appreciate ideas with INFOGRAPHIC
(3) Design of the presentation is up to the company logo in all variations. ( attached files).
(4) We would like to see designs that use grey, blue, orange and maroon colors - corporate colors of our logo.
Nice to have
• Infografics
Designs we like:
to brintaly.com+; zumoth.com; pelvanstudio.com; tarnowatt.co.uk (infografics)

```html
<!DOCTYPE html>
<html lang="en">
<head>
<meta charset="utf-8">
<title>KORVALE — Our Products</title>
<link rel="stylesheet" href="https://fonts.googleapis.com/css2?family=Bebas+Neue&family=Open+Sans:wght@400;600&display=swap">
<style>
  :root {
    --blue: #4a77b4;
    --blue-band: #4676b5;
    --orange: #f79646;
    --bg: #f2f2f2;
    --ring: #ffffff;
    --well-light: #f3f3f3;
    --well-dark: #dadada;
    --footer-text: #ffffff;
  }
  html, body {
    margin: 0;
    padding: 0;
    width: 1200px;
    height: 900px;
    overflow: hidden;
    background: var(--bg);
  }
  .slide {
    position: relative;
    width: 1200px;
    height: 900px;
    background: var(--bg);
    overflow: hidden;
  }
  .slide-art {
    position: absolute;
    inset: 0;
    width: 1200px;
    height: 900px;
  }
  .title-marker { fill: var(--orange); }
  .slide-title {
    font-family: "Bebas Neue", "Oswald", sans-serif;
    font-size: 66px;
    fill: var(--blue);
    letter-spacing: 0.5px;
  }
  .brand-name {
    font-family: "Bebas Neue", "Oswald", sans-serif;
    font-size: 52px;
    fill: var(--blue);
    letter-spacing: 2px;
  }
  .brand-mark { fill: var(--blue); }
  .ring { fill: var(--ring); }
  .well { fill: url(#wellShade); }
  .step-number {
    font-family: "Bebas Neue", "Oswald", sans-serif;
    text-anchor: middle;
    dominant-baseline: central;
  }
  .product-label {
    font-family: "Bebas Neue", "Oswald", sans-serif;
    font-size: 48px;
    letter-spacing: 0.3px;
  }
  .tone-blue { fill: var(--blue); }
  .tone-orange { fill: var(--orange); }
  .leader-blue { stroke: var(--blue); stroke-width: 1.4; }
  .leader-orange { stroke: var(--orange); stroke-width: 1.4; }
  .icon-placeholder { fill: var(--blue); opacity: 0.8; }
  .footer-band { fill: var(--blue-band); }
  .footer-note {
    font-family: "Open Sans", sans-serif;
    font-size: 14px;
    fill: var(--footer-text);
  }
  .page-number {
    font-family: "Open Sans", sans-serif;
    font-weight: 600;
    font-size: 24px;
    fill: var(--footer-text);
    text-anchor: middle;
  }
</style>
</head>
<body>
<main class="slide">
  <svg class="slide-art" viewBox="0 0 1200 900" xmlns="http://www.w3.org/2000/svg">
    <defs>
      <filter id="ringShadow" x="-30%" y="-30%" width="160%" height="160%">
        <feDropShadow dx="0" dy="5" stdDeviation="7" flood-color="#000" flood-opacity="0.22"/>
      </filter>
      <radialGradient id="wellShade" cx="50%" cy="45%" r="55%">
        <stop offset="0%" stop-color="var(--well-light)"/>
        <stop offset="78%" stop-color="#ececec"/>
        <stop offset="100%" stop-color="var(--well-dark)"/>
      </radialGradient>
    </defs>

    <rect class="title-marker" x="10" y="0" width="55" height="94"/>
    <text class="slide-title" x="79" y="73">OUR PRODUCTS</text>

    <g class="brand">
      <rect class="brand-mark" x="1010" y="30" width="24" height="24"/>
      <text class="brand-name" x="1166" y="64" text-anchor="end">KORVALE</text>
    </g>

    <g class="leaders">
      <line class="leader-blue" x1="120" y1="800" x2="290" y2="800"/>
      <circle class="tone-blue" cx="120" cy="800" r="4"/>
      <line class="leader-orange" x1="515" y1="724" x2="956" y2="724"/>
      <circle class="tone-orange" cx="956" cy="724" r="4"/>
      <line class="leader-blue" x1="222" y1="566" x2="515" y2="566"/>
      <circle class="tone-blue" cx="222" cy="566" r="4"/>
      <line class="leader-orange" x1="815" y1="499" x2="1119" y2="499"/>
      <circle class="tone-orange" cx="1119" cy="499" r="4"/>
      <line class="leader-blue" x1="511" y1="296" x2="805" y2="296"/>
      <circle class="tone-blue" cx="511" cy="296" r="4"/>
    </g>

    <g class="step step-5">
      <circle class="ring" cx="921" cy="273" r="123" filter="url(#ringShadow)"/>
      <circle class="well" cx="921" cy="273" r="90"/>
      <text class="step-number tone-blue" x="921" y="276" font-size="64">05</text>
    </g>
    <g class="step step-4">
      <circle class="ring" cx="741" cy="425" r="104" filter="url(#ringShadow)"/>
      <circle class="well" cx="741" cy="425" r="75"/>
      <text class="step-number tone-orange" x="741" y="428" font-size="52">04</text>
    </g>
    <g class="step step-3">
      <circle class="ring" cx="594" cy="548" r="89" filter="url(#ringShadow)"/>
      <circle class="well" cx="594" cy="548" r="65"/>
      <text class="step-number tone-blue" x="594" y="551" font-size="46">03</text>
    </g>
    <g class="step step-2">
      <circle class="ring" cx="462" cy="665" r="84" filter="url(#ringShadow)"/>
      <circle class="well" cx="462" cy="665" r="60"/>
      <text class="step-number tone-orange" x="462" y="668" font-size="42">02</text>
    </g>
    <g class="step step-1">
      <circle class="ring" cx="339" cy="760" r="66" filter="url(#ringShadow)"/>
      <circle class="well" cx="339" cy="760" r="48"/>
      <text class="step-number tone-blue" x="339" y="763" font-size="38">01</text>
    </g>

    <text class="product-label tone-blue" x="130" y="790">SERVICE</text>
    <text class="product-label tone-orange" x="572" y="715">NON- STANDARD SERVICES</text>
    <text class="product-label tone-blue" x="225" y="556">MICE &amp; CONGRESS</text>
    <text class="product-label tone-orange" x="860" y="481">BUSINESS TRAVEL</text>
    <text class="product-label tone-blue" x="519" y="281">ON-LINE BOOKING</text>

    <rect class="icon-placeholder" x="144" y="696" width="96" height="40" rx="6"
          role="img" aria-label="Pictogram of two people exchanging service"/>
    <rect class="icon-placeholder" x="306" y="436" width="94" height="58" rx="6"
          role="img" aria-label="Pictogram of people meeting around a table"/>
    <rect class="icon-placeholder" x="590" y="140" width="95" height="79" rx="6"
          role="img" aria-label="Pictogram of a person booking at a laptop"/>

    <g class="icon-gears" aria-label="Gears icon">
      <circle cx="756" cy="617" r="15" fill="none" stroke="var(--orange)" stroke-width="9" stroke-dasharray="7 5.5"/>
      <circle cx="756" cy="617" r="12" fill="none" stroke="var(--orange)" stroke-width="7"/>
      <circle cx="786" cy="643" r="10" fill="none" stroke="var(--orange)" stroke-width="7" stroke-dasharray="5 4.3"/>
      <circle cx="786" cy="643" r="8" fill="none" stroke="var(--orange)" stroke-width="5"/>
    </g>

    <g class="icon-plane" aria-label="Airplane icon">
      <path class="tone-orange" transform="translate(1031 408) rotate(-40)"
            d="M-26 -3 L-4 -3 L8 -22 L14 -22 L8 -3 L20 -3 L25 -10 L29 -10 L27 0 L29 10 L25 10 L20 3 L8 3 L14 22 L8 22 L-4 3 L-26 3 Q-30 0 -26 -3 Z"/>
    </g>

    <rect class="footer-band" x="0" y="854" width="1200" height="46"/>
    <polygon class="footer-band" points="1088,855 1125,827 1162,855"/>
    <text class="footer-note" x="18" y="884">Copyright 2014. KORVALE . All Rights reserved</text>
    <text class="page-number" x="1128" y="873">1</text>
  </svg>
</main>
</body>
</html>
```